Brim Contractors

We are a group of people that doing a picking fruits like Oranges and grapes seasonal. We would like to have the colors " light black or black " back ground of the card. Thanks

Industry/Entity Type

Group

Contact Information for Business Card

Mob 0498213564 . Fax 03 5187 3940. P.O.Box 517 Tarrawong Vic 3461

```html
<!DOCTYPE html>
<html lang="en">
<head>
<meta charset="utf-8">
<title>Brim Contractors – Business Card</title>
<link rel="stylesheet" href="https://fonts.googleapis.com/css2?family=Archivo+Black&display=swap">
<style>
  :root {
    --page-bg: #3a2a1f;
    --card-bg: #070605;
    --gold: #d9962a;
    --orange: #d4561c;
    --orange-deep: #b8441a;
    --fruit-orange: #c9521f;
    --fruit-gold: #c98a22;
  }
  html, body {
    margin: 0;
    padding: 0;
    width: 1200px;
    height: 900px;
    overflow: hidden;
    background: var(--page-bg);
  }
  .card {
    position: absolute;
    left: 110px;
    top: 170px;
    width: 980px;
    height: 560px;
    background: var(--card-bg);
    border-radius: 34px;
    font-family: "Archivo Black", "Arial Black", sans-serif;
    overflow: hidden;
  }
  .brand {
    position: absolute;
    left: 90px;
    top: 150px;
  }
  .brand-name {
    margin: 0;
    font-size: 56px;
    line-height: 1;
    color: var(--gold);
    font-weight: 400;
    letter-spacing: 1px;
    white-space: nowrap;
  }
  .services {
    margin: 14px 0 0 4px;
    font-size: 19px;
    color: var(--gold);
    letter-spacing: 1px;
    display: flex;
    align-items: center;
    gap: 10px;
    white-space: nowrap;
  }
  .services .dot {
    width: 10px;
    height: 10px;
    border-radius: 50%;
    background: var(--orange);
    display: inline-block;
  }
  .fruit {
    position: absolute;
    border-radius: 50%;
  }
  .fruit--orange {
    left: 540px;
    top: 42px;
    width: 84px;
    height: 84px;
    background: radial-gradient(circle at 40% 40%, var(--fruit-orange), #6e2a10);
  }
  .fruit--grape {
    left: 690px;
    top: 112px;
    width: 96px;
    height: 90px;
    background: radial-gradient(circle at 45% 40%, var(--fruit-gold), #5e3e0e);
  }
  .contact {
    position: absolute;
    left: 150px;
    top: 360px;
    padding-left: 30px;
    border-left: 4px solid var(--orange);
    padding-top: 6px;
    padding-bottom: 28px;
  }
  .contact-line {
    display: flex;
    align-items: center;
    gap: 14px;
    font-size: 26px;
    color: var(--gold);
    line-height: 1.3;
    letter-spacing: 1px;
  }
  .contact-line svg {
    width: 20px;
    height: 22px;
    flex: none;
  }
  .address-rule {
    position: absolute;
    left: 520px;
    right: 0;
    top: 385px;
    height: 3px;
    background: var(--orange-deep);
  }
  .address {
    position: absolute;
    right: 40px;
    top: 405px;
    margin: 0;
    font-size: 24px;
    color: var(--gold);
    letter-spacing: 1px;
    font-style: normal;
    white-space: nowrap;
  }
</style>
</head>
<body>
  <main class="card">
    <div class="fruit fruit--orange" role="img" aria-label="Cartoon orange illustration"></div>
    <div class="fruit fruit--grape" role="img" aria-label="Cartoon fruit illustration"></div>

    <header class="brand">
      <h1 class="brand-name">Brim Contractors</h1>
      <p class="services">
        <span>Citrus Picking</span><span class="dot"></span>
        <span>Grapes Picking</span><span class="dot"></span>
        <span>Pruning</span>
      </p>
    </header>

    <section class="contact">
      <div class="contact-line">
        <svg viewBox="0 0 20 22" aria-label="Mobile">
          <rect x="5" y="1" width="10" height="20" rx="2" fill="none" stroke="var(--orange)" stroke-width="2"/>
          <rect x="8" y="17" width="4" height="2" fill="var(--orange)"/>
        </svg>
        <span>0498213564</span>
      </div>
      <div class="contact-line">
        <svg viewBox="0 0 20 22" aria-label="Fax">
          <rect x="5" y="2" width="10" height="7" fill="none" stroke="var(--orange)" stroke-width="2"/>
          <rect x="1" y="9" width="18" height="9" rx="2" fill="var(--orange)"/>
          <rect x="5" y="14" width="10" height="6" fill="var(--card-bg)" stroke="var(--orange)" stroke-width="1.5"/>
        </svg>
        <span>03 5187 3940</span>
      </div>
    </section>

    <div class="address-rule"></div>
    <address class="address">P.O.Box 517 Tarrawong Vic 3461</address>
  </main>
</body>
</html>
```